Packaged Food Business Needs a Packaging Design

We need a package design to be used as a label/sticker on the lids of round and square transparent plastic containers and on the sides of resealable stand-up pouches. The brand name is 'Savourly' - please find attached logo together with pictures of the sample containers and pouch. We will use the packaging to market a wide variety of food categories from nuts, dried fruits, spices, cooking chocolates, baking ingredients, cereals, grains and pulses.

OVERALL FEEDBACK ON DESIGNS ALREADY RECEIVED:

- We have found so far that a lot of our mandatory requirements are not adhered to in designs that have been submitted so far. We would like to emphasise that the ingredient, weight and expiry text will be printed at the time of packing so it should not take prime space on the pack BUT at the same time some 'blank' space needs to flawlessly be incorporated into the overall design for this purpose
- We encourage you to glorify the brand logo in the pack, and absolutely refrain from duplicating the tagline
- Please note that ONE label design will be used to pack a wide variety of food ingredients and therefore please ensure that the choice of your design incorporates this requirement, in the past we have received designs that are limited to only one type of food (like nuts) or have received designs that are too floral or leafy (and not grounded to food
- Please ensure that you submit designs for all three packaging formats, it is critical to see the family look from the on-set

Target Market(s)

The brand is targeting both mothers and professional chefs and therefore the label design should be broadly approachable and convey affordable premium

Industry/Entity Type

Business

Requirements
Must have
• - Consistent with the brand name and logo, the overall look and feel of the packaging should convey values of healthy, gourmet food ingredients, high in nourishment and project a sense of delightful taste
• - The design styling to be modern and 'simplistic' (embracing 'less-is-more' type of a design style)
• - Design a packaging architecture that incorporates the brand logo together with its tagline lock-up of 'taste the goodness in every spoonful' - find logo attached
• - The design needs to have a dedicated area to print the ingredient (e.g., Mixed Nuts), weight (e.g., 500g) and expiry (this space needs to be flawlessly incorporated into the design) - this information will be printed either with an inkjet printer or with a rubber stamp so please leave an empty space (the text should not be part of the design, just the area for the text needs to be included in the design)
• - The packaging must include 'Packed By: Mwenda Traders Ltd, P. O. Box 41562, Kampala - Uganda'
• - For the design of the resealable pouch, please incorporate a window to see through the ingredients and a hole on top to hang on supermarket pegs if necessary
Nice to have
• - We would love to have some design submissions that are bold and cheerful and fun (but not frivolous) - please see attached inspiration for 'fun' packaging. The attachments are purely for inspiration, not to infringe on anyone else's TM and copyrights
• - Incorporate green to convey healthy, organic values
• - Explore use of gold and silver convey premiumness
Should not have
• - Do not duplicate the tagline
• - Do not include the ingredient, weight and expiry in the main graphic of the design, these will be printed at the time of packing so ensure there is provision for this in a flawless way in the design (e.g., via a blank space allocated for this purpose)

```html
<!DOCTYPE html>
<html lang="en">
<head>
<meta charset="utf-8">
<title>Savourly Label</title>
<link rel="stylesheet" href="https://fonts.googleapis.com/css2?family=Bebas+Neue&family=Josefin+Sans:wght@600&family=Open+Sans:wght@800&family=Source+Sans+3:wght@400&display=swap">
<style>
  :root {
    --leaf-green: #a8cf45;
    --deep-green: #5ea81a;
    --tag-green: #4f8a1c;
    --cream: #f2efd4;
    --soil: #42220a;
    --ink: #3b1e0b;
    --gold: #d4bd1e;
    --window: #ffffff;
    --footer-ink: #b8713c;
  }
  html, body {
    margin: 0;
    padding: 0;
    width: 825px;
    height: 1200px;
    overflow: hidden;
    background: var(--leaf-green);
  }
  .label {
    position: relative;
    width: 825px;
    height: 1200px;
  }
  .label-art {
    position: absolute;
    inset: 0;
    display: block;
  }
  .brand-lockup {
    position: absolute;
    left: 39px;
    right: 39px;
    top: 200px;
    text-align: center;
  }
  .brand-name {
    margin: 0;
    font-family: "Bebas Neue", "Oswald", sans-serif;
    font-size: 118px;
    line-height: 1;
    letter-spacing: 10px;
    color: var(--ink);
    font-weight: 400;
  }
  .brand-tagline {
    margin: 6px 0 0;
    font-family: "Josefin Sans", sans-serif;
    font-weight: 600;
    font-size: 19px;
    letter-spacing: 2.6px;
    text-transform: uppercase;
    color: var(--tag-green);
  }
  .packer-line {
    position: absolute;
    left: 39px;
    right: 39px;
    top: 1124px;
    margin: 0;
    text-align: center;
    font-family: "Source Sans 3", "Myriad Pro", sans-serif;
    font-size: 16px;
    color: var(--footer-ink);
  }
  .window-caption {
    font-family: "Open Sans", sans-serif;
    font-weight: 800;
    font-size: 21px;
    fill: var(--ink);
  }
</style>
</head>
<body>
<main class="label">
  <svg class="label-art" width="825" height="1200" viewBox="0 0 825 1200" aria-hidden="false">
    <defs>
      <linearGradient id="foliage-tones" x1="0" y1="0" x2="0" y2="1">
        <stop offset="0" stop-color="#a8cf45"/>
        <stop offset="0.55" stop-color="#5ea81a"/>
        <stop offset="1" stop-color="#42220a"/>
      </linearGradient>
      <path id="caption-arc" d="M272 496 A160 160 0 0 1 552 496"/>
    </defs>

    <!-- inner panel: green hill band -->
    <rect class="hill-band" x="39" y="39" width="747" height="680" fill="var(--leaf-green)"/>

    <!-- cream sky with flowing lower edge -->
    <path class="sky-panel" fill="var(--cream)"
          d="M39 39 H786 V530 C700 545 600 562 520 592 C430 626 350 668 250 665 C150 662 90 632 39 600 Z"/>

    <!-- gold bookmark ribbon -->
    <path class="gold-ribbon" fill="var(--gold)" d="M710 39 H746 V285 L728 268 L710 285 Z"/>

    <!-- soil base -->
    <rect class="soil-base" x="39" y="708" width="747" height="449" fill="var(--soil)"/>

    <!-- foliage fringe area -->
    <rect class="foliage-fringe" x="39" y="708" width="747" height="210" fill="url(#foliage-tones)" opacity="0.55"
          role="img" aria-label="Row of stylised green leaves hanging over the brown soil band"/>

    <!-- see-through window ring -->
    <circle class="window-ring" cx="412" cy="570" r="177" fill="var(--leaf-green)"/>
    <circle class="window-opening" cx="412" cy="576" r="140" fill="var(--window)"/>
    <path class="window-hill" fill="var(--leaf-green)"
          d="M272 660 C340 640 420 590 520 592 C560 592 580 600 600 610 L600 760 L272 760 Z"/>
    <circle class="window-ring-lower" cx="412" cy="570" r="177" fill="none" stroke="var(--leaf-green)" stroke-width="0"/>

    <text class="window-caption">
      <textPath href="#caption-arc" startOffset="50%" text-anchor="middle">LOOK INSIDE!</textPath>
    </text>
  </svg>

  <header class="brand-lockup">
    <h1 class="brand-name">SAVOURLY</h1>
    <p class="brand-tagline">Taste the goodness in every spoonful!</p>
  </header>

  <p class="packer-line">Packed By: Mwenda Traders Ltd, P. O. Box 41562, Kampala - Uganda</p>
</main>
</body>
</html>
```